LedgaVue Business Card

We need a business card design using the attached logo. The company is a financial services company that provides a dashboard (chart based information) for Executives of small businesses to use to better manage their information. The design must be progressive, make good utilization of the logo and project stability and financial security.

Industry/Entity Type

Financial

```html
<!DOCTYPE html>
<html lang="en">
<head>
<meta charset="utf-8">
<title>LedgaVue Business Card</title>
<link href="https://fonts.googleapis.com/css2?family=Open+Sans:wght@400;600&display=swap" rel="stylesheet">
<style>
  :root {
    --canvas: #ecebe8;
    --brand-red: #c8323c;
    --brand-red-dark: #9e1c26;
    --brand-red-light: #d8474f;
    --ink: #3a3a3c;
    --muted: #8a8a8c;
    --paper: #ffffff;
  }
  * { margin: 0; padding: 0; box-sizing: border-box; }
  html, body { width: 1200px; height: 800px; overflow: hidden; }
  body {
    background: var(--canvas);
    font-family: "Open Sans", Arial, sans-serif;
    position: relative;
  }

  /* Back of card */
  .card-back {
    position: absolute;
    left: 90px; top: 110px;
    width: 340px; height: 580px;
    background: linear-gradient(160deg, var(--brand-red-light) 0%, var(--brand-red) 45%, var(--brand-red-dark) 100%);
    box-shadow: 0 10px 30px rgba(0,0,0,.18);
    overflow: hidden;
  }
  .card-back__name {
    position: absolute;
    left: 70px; bottom: 40px;
    transform-origin: left bottom;
    transform: rotate(-90deg) translateY(100%);
    color: var(--paper);
    font-size: 96px;
    font-weight: 600;
    letter-spacing: -2px;
    line-height: 1;
    white-space: nowrap;
  }

  /* Front of card */
  .card-front {
    position: absolute;
    left: 530px; top: 230px;
    width: 580px; height: 340px;
    background: var(--paper);
    box-shadow: 0 10px 30px rgba(0,0,0,.18);
    overflow: hidden;
  }
  .brand {
    position: absolute;
    left: 40px; top: 34px;
    display: flex; align-items: center; gap: 12px;
  }
  .brand__mark {
    width: 30px; height: 30px;
    background: var(--brand-red);
  }
  .brand__name {
    font-size: 40px;
    font-weight: 600;
    color: var(--ink);
    letter-spacing: -1px;
    line-height: 1;
  }
  .contact {
    position: absolute;
    left: 40px; top: 100px;
  }
  .contact__name {
    color: var(--brand-red);
    font-size: 19px;
    font-weight: 600;
    text-transform: uppercase;
    letter-spacing: .5px;
  }
  .contact__role {
    color: var(--muted);
    font-size: 12px;
    margin-bottom: 8px;
  }
  .contact__list { list-style: none; }
  .contact__item {
    display: flex; align-items: center; gap: 8px;
    font-size: 12.5px;
    color: var(--ink);
    line-height: 20px;
  }
  .contact__icon {
    width: 14px; height: 14px;
    background: var(--brand-red);
    border-radius: 2px;
    display: flex; align-items: center; justify-content: center;
  }
  .contact__address {
    font-size: 12.5px;
    color: var(--ink);
    line-height: 18px;
    margin-top: 6px;
    text-transform: uppercase;
  }
  .web-band {
    position: absolute;
    left: 0; bottom: 0;
    width: 100%; height: 40px;
    background: linear-gradient(90deg, var(--brand-red-dark), var(--brand-red));
    display: flex; align-items: center;
    padding-left: 40px;
  }
  .web-band__url {
    color: #2a1a1c;
    font-size: 13px;
    font-weight: 600;
    letter-spacing: 4px;
  }
</style>
</head>
<body>

<section class="card-back" aria-label="Card back">
  <div class="card-back__name">LedgaVue</div>
</section>

<section class="card-front" aria-label="Card front">
  <div class="brand">
    <span class="brand__mark"></span>
    <span class="brand__name">LedgaVue</span>
  </div>

  <div class="contact">
    <p class="contact__name">Dana Whitfield</p>
    <p class="contact__role">Principal</p>
    <ul class="contact__list">
      <li class="contact__item">
        <span class="contact__icon">
          <svg width="10" height="10" viewBox="0 0 10 10"><path d="M2 1h2l1 2-1.2 1A5 5 0 0 0 6 6.2L7 5l2 1v2c0 .6-.4 1-1 1A8 8 0 0 1 1 2c0-.6.4-1 1-1z" fill="#fff"/></svg>
        </span>555-201-4410
      </li>
      <li class="contact__item">
        <span class="contact__icon">
          <svg width="10" height="10" viewBox="0 0 10 10"><rect x="2.5" y="0.5" width="5" height="9" rx="1" fill="none" stroke="#fff"/><circle cx="5" cy="7.6" r=".7" fill="#fff"/></svg>
        </span>555-201-4478
      </li>
      <li class="contact__item">
        <span class="contact__icon">
          <svg width="10" height="10" viewBox="0 0 10 10"><rect x="1" y="2.5" width="8" height="5.5" fill="none" stroke="#fff"/><path d="M1 2.5l4 3 4-3" fill="none" stroke="#fff"/></svg>
        </span>d.whitfield@ledgavueconsulting.com
      </li>
    </ul>
    <p class="contact__address">4180 Marlow Ave<br>Fairview, TX 75000</p>
  </div>

  <div class="web-band">
    <span class="web-band__url">www.ledgavue.com</span>
  </div>
</section>

</body>
</html>
```